Restoration Specialist in need of business card designs

One side of the business card is a bathroom ripped out down to the studs with just a sink and toilet and then the other side is the bathroom (same sink and toilet) but put back together. Like a before and after on each side behind our information. Stand out, hard to forget, business cards for my restoration company. I want a unique concept all together.
Must include in no particular order:
our business name "Summit Renewals"
Possible Logo for a restoration company
Owner; Dennis Moravec
410-386-7294
dmoravec@summitrenewalsqx.example
SummitRenewalsQX.example (our company website) BUT I am open to any and all designs and options.

Target Market(s)

Customers, Men in the mitigation, plumbing, electrical, HVAC, Roofing, insurance companies

Industry/Entity Type

Restoration/ construction

Contact Information for Business Card

Must include in no particular order: our business name "Summit Renewals" Owner; Dennis Moravec 410-386-7294 dmoravec@summitrenewalsqx.example SummitRenewalsQX.example (our company website) MAY include a list of our services: Residential~ Emergency Response ~ Board- up~ Complete Restoration

Font styles to use
Serif

Colors
0054AA
0677BA
7BADD7
CADEEF
E8F1F8
F0912C
F2A743
F7CA91
FBE8D2
FDF5EE

Requirements
Must have
• unique, memorable, not something men have seen over and over again,
Nice to have
• eye catching
Should not have
• Been something I could have made by myself

```html
<!DOCTYPE html>
<html lang="en">
<head>
<meta charset="utf-8">
<title>Summit Renewals – Business Card</title>
<link href="https://fonts.googleapis.com/css2?family=Libre+Baskerville:wght@700&family=Rubik:wght@500;600&display=swap" rel="stylesheet">
<style>
  :root {
    --backdrop: #c9c9c9;
    --navy: #15344f;
    --navy-deep: #0f2a41;
    --orange: #ee7a22;
    --white: #ffffff;
    --ink: #1c3550;
  }
  * { box-sizing: border-box; margin: 0; padding: 0; }
  html, body { width: 1200px; height: 900px; overflow: hidden; }
  body {
    background: var(--backdrop);
    position: relative;
    font-family: "Rubik", Arial, sans-serif;
  }
  .card {
    position: absolute;
    width: 700px;
    height: 400px;
    border-radius: 34px;
    overflow: hidden;
    box-shadow: 0 10px 24px rgba(0,0,0,0.28);
  }
  .card--front { left: 70px; top: 50px; background: linear-gradient(135deg, var(--navy) 0%, var(--navy-deep) 100%); }
  .card--back { left: 430px; top: 450px; background: var(--white); }

  .brand {
    position: absolute;
    display: flex;
    align-items: flex-start;
    gap: 14px;
  }
  .brand__mark { width: 22px; height: 22px; background: var(--orange); margin-top: 12px; flex: none; }
  .brand__name {
    font-family: "Libre Baskerville", Georgia, serif;
    font-weight: 700;
    color: var(--orange);
    font-size: 52px;
    line-height: 1.05;
    text-transform: uppercase;
    letter-spacing: 1px;
  }
  .brand__rule { position: absolute; height: 4px; }
  .card--front .brand { left: 60px; top: 70px; }
  .card--front .brand__rule { left: 96px; top: 210px; width: 300px; background: var(--white); }
  .card--back .brand { left: 60px; top: 60px; }
  .card--back .brand__rule { left: 96px; top: 200px; width: 300px; background: var(--navy); }

  .services {
    position: absolute;
    list-style: none;
    color: var(--white);
    font-weight: 600;
    font-size: 19px;
    line-height: 1.55;
  }
  .services li { display: flex; align-items: center; gap: 12px; }
  .services li::before {
    content: "";
    width: 10px; height: 10px;
    background: var(--orange);
    box-shadow: inset 0 0 0 2px var(--orange), inset 0 0 0 3px var(--white);
    flex: none;
  }
  .services--primary { left: 96px; top: 250px; }
  .services--secondary { left: 400px; top: 250px; }

  .holder { position: absolute; left: 126px; top: 224px; }
  .holder__name {
    font-family: "Libre Baskerville", Georgia, serif;
    font-weight: 700;
    color: var(--ink);
    font-size: 30px;
    letter-spacing: 1px;
    text-transform: uppercase;
  }
  .holder__role { color: var(--orange); font-weight: 600; font-size: 21px; margin-top: 2px; }
  .accent-tab { position: absolute; left: 90px; top: 232px; width: 22px; height: 38px; background: var(--orange); }

  .contact {
    position: absolute;
    left: 126px; top: 302px;
    list-style: none;
    color: var(--ink);
    font-weight: 500;
    font-size: 19px;
    line-height: 1.5;
  }
  .contact li { display: flex; align-items: center; gap: 12px; }
  .contact svg { width: 20px; height: 20px; flex: none; }
</style>
</head>
<body>

  <section class="card card--front" aria-label="Business card front">
    <div class="brand">
      <span class="brand__mark"></span>
      <span class="brand__name">Summit<br>Renewals</span>
    </div>
    <span class="brand__rule"></span>
    <ul class="services services--primary">
      <li>Residential</li>
      <li>Emergency Response</li>
      <li>Board- up</li>
    </ul>
    <ul class="services services--secondary">
      <li>Storm Protection</li>
      <li>Complete Restoration</li>
    </ul>
  </section>

  <section class="card card--back" aria-label="Business card back">
    <div class="brand">
      <span class="brand__mark"></span>
      <span class="brand__name">Summit<br>Renewals</span>
    </div>
    <span class="brand__rule"></span>

    <span class="accent-tab"></span>
    <div class="holder">
      <p class="holder__name">Dennis Moravec</p>
      <p class="holder__role">Owner</p>
    </div>

    <ul class="contact">
      <li>
        <svg viewBox="0 0 24 24" aria-hidden="true"><path fill="#ee7a22" d="M6.6 10.8a15.1 15.1 0 0 0 6.6 6.6l2.2-2.2a1 1 0 0 1 1-.25 11.4 11.4 0 0 0 3.6.57 1 1 0 0 1 1 1V20a1 1 0 0 1-1 1A17 17 0 0 1 3 4a1 1 0 0 1 1-1h3.5a1 1 0 0 1 1 1c0 1.25.2 2.45.57 3.57a1 1 0 0 1-.25 1z"/></svg>
        410-386-7294
      </li>
      <li>
        <svg viewBox="0 0 24 24" aria-hidden="true"><rect x="2" y="5" width="20" height="14" rx="1.5" fill="#ee7a22"/><path d="M3 6.5l9 6.5 9-6.5" fill="none" stroke="#fff" stroke-width="1.8"/></svg>
        dmoravec@summitrenewalsqx.example
      </li>
      <li>
        <svg viewBox="0 0 24 24" aria-hidden="true"><g fill="none" stroke="#ee7a22" stroke-width="2"><circle cx="12" cy="12" r="9.5"/><ellipse cx="12" cy="12" rx="4" ry="9.5"/><path d="M2.5 12h19M4 7h16M4 17h16"/></g></svg>
        SummitRenewalsQX.example
      </li>
    </ul>
  </section>

</body>
</html>
```